Trade two share two natural Lather Company,

I'm looking for a one page responsive web site that will have the ability to order the soap direct from the site. TrTr lather company (trade tw, share two) will be giving away a bar of soap to the needy for every purchase. Similar to what Rik's boots does. The site look and feel is vintage/organic. ive attached a couple links that have the look and feel. I am looking for designers that want to make this a fully functional website that is ready to launch upon completion. The budget will be increase for anyone that wants to make the site fully functional and ready to have it hosted. Thank you. Attaching our logo and some background photos.

http://www.layoutfarmex.com/demo/71234.html

http://www.layoutfarmex.com/demo/72345.html

http://www.layoutfarmex.com/demo/73456.html

Target Market(s)

Anyone that uses or considers natural soap as the best way to clean themselves with out the harsh chemicals.

Industry/Entity Type

It Company

Coding

Coded - Design and coding required

Font styles to use
Serif
Sans Serif

Requirements
Must have
• Ability to purchase soap on the site, organic vintage look.T
Should not have
• Cheesy clip art. As far as the color, I am thinking a vintage washed out look.

```html
<!DOCTYPE html>
<html lang="en">
<head>
<meta charset="utf-8">
<title>TrTr lather company</title>
<link href="https://fonts.googleapis.com/css2?family=Raleway:wght@400;500;600;700&family=Lato:wght@400;700&display=swap" rel="stylesheet">
<style>
:root{
  --wood:#6e5646;
  --wood-dark:#4f3d31;
  --sky:#7fb2d6;
  --sky-deep:#4f8ab6;
  --sky-pale:#d6e8f4;
  --white:#ffffff;
  --slate:#7c7975;
  --forest:#2c3530;
  --paper:#d9d0c3;
  --ink:#3a3836;
  --card:#f1f1f1;
  --footer:#3d3733;
  --footer-bottom:#26221f;
  --muted:#c9c3bd;
}
*{box-sizing:border-box;margin:0;padding:0}
html,body{width:1200px;height:2341px;overflow:hidden}
body{position:relative;font-family:'Lato',sans-serif;color:var(--white);background:var(--footer-bottom)}
.abs{position:absolute}
section,header,footer{position:absolute;left:0;width:1200px}

/* header */
.site-header{top:0;height:190px;background:repeating-linear-gradient(90deg,var(--wood) 0 58px,var(--wood-dark) 58px 60px,#765e4d 60px 118px,var(--wood-dark) 118px 120px)}
.brand{left:105px;top:22px;display:flex;align-items:center;gap:10px}
.brand-dot{width:22px;height:22px;border-radius:50%;background:var(--sky)}
.brand-name{font-family:'Raleway',sans-serif;font-weight:600;font-size:34px;color:var(--sky);line-height:1}
.brand-sub{left:137px;top:66px;font-family:'Raleway',sans-serif;font-weight:600;font-size:13px;letter-spacing:4px;color:var(--sky)}
.util-box{background:var(--sky);border:1px solid var(--sky-pale);color:var(--white);font-size:12px;font-weight:700;text-align:center}
.login{left:766px;top:20px;width:137px;height:27px;line-height:25px}
.currency{left:766px;top:52px;width:137px;height:51px;padding-top:6px}
.currency .select{display:inline-block;margin-top:5px;border:1px solid var(--white);border-radius:8px;padding:0 10px;font-weight:400;font-size:11px}
.cart{left:922px;top:18px;width:180px;height:92px;background:var(--white);border-radius:4px;box-shadow:0 2px 4px rgba(0,0,0,.35)}
.cart-label{position:absolute;left:0;top:0;width:180px;height:26px;background:var(--sky);color:var(--white);font-family:'Raleway',sans-serif;font-weight:700;font-size:15px;text-align:center;line-height:26px;border-radius:4px 4px 0 0}
.cart-count{position:absolute;left:50px;top:36px;font-size:40px;color:var(--sky-deep);line-height:1}
.cart-text{position:absolute;left:78px;top:44px;font-size:14px;font-weight:700;color:var(--sky-deep);line-height:15px}
.nav{left:98px;top:130px;width:1004px;height:42px;border-radius:12px;background:linear-gradient(var(--sky),var(--sky-deep));box-shadow:0 3px 5px rgba(0,0,0,.35)}
.nav a{position:absolute;top:0;line-height:42px;color:var(--white);font-size:16px;font-weight:700;text-decoration:none;transform:translateX(-50%)}
.nav .sep{position:absolute;top:4px;width:2px;height:34px;background:rgba(255,255,255,.55)}

/* hero */
.hero{top:190px;height:497px;background:linear-gradient(110deg,#8c8a86 0%,#cfcbc2 30%,#e8e2c8 55%,#d7d1b1 75%,#6d7c5a 100%)}
.hero-caption{left:98px;top:216px;width:500px;height:117px;background:rgba(40,40,40,.55);padding:14px 10px}
.hero-caption h1{font-family:'Raleway',sans-serif;font-weight:400;font-size:42px;color:var(--sky);line-height:1}
.hero-caption p{font-family:'Raleway',sans-serif;font-size:37px;color:var(--white);line-height:1.25}
.btn{display:block;position:absolute;background:var(--sky);border:2px solid var(--sky-pale);color:var(--white);font-size:12px;letter-spacing:1.5px;text-align:center}
.hero .btn{left:100px;top:358px;width:128px;height:37px;line-height:33px}
.slide-arrow{width:36px;height:34px;background:#2b2b2b;border:1px solid #999}

/* section titles */
.title{font-family:'Raleway',sans-serif;font-weight:700;font-size:37px;line-height:1}

/* about */
.about{top:687px;height:332px;background:linear-gradient(#8a8682,var(--slate) 60%,#8d8781)}
.about .title{left:105px;top:43px;color:var(--white)}
.about-text{left:115px;top:118px;width:970px;text-align:center;font-size:14px;letter-spacing:.55px;line-height:22px;color:var(--white)}
.about .btn{left:535px;top:229px;width:128px;height:36px;line-height:32px}

/* products */
.products{top:1019px;height:565px;background:linear-gradient(100deg,#4b4a3a 0%,var(--forest) 40%,#34403a 75%,#3b4d45 100%)}
.products .title{left:105px;top:50px;color:var(--sky)}
.products .rule{left:105px;top:98px;width:365px;height:1px;background:var(--sky)}
.product{position:absolute;top:134px;width:298px}
.product-photo{width:298px;height:272px;border:4px solid var(--sky)}
.product h3{margin-top:18px;text-align:center;font-family:'Raleway',sans-serif;font-weight:600;font-size:21px;color:var(--sky)}
.product-meta{display:flex;justify-content:space-between;padding:0 48px 0 46px;margin-top:12px;font-size:10px;align-items:center}
.product-meta b{font-size:14px}
.quick{text-align:center;font-size:10px;letter-spacing:2px;margin-top:11px}

/* blog */
.blog{top:1584px;height:441px;background:radial-gradient(ellipse at 50% 40%,#e3dbcf,var(--paper) 60%,#c8bca9)}
.blog .title{left:100px;top:44px;color:var(--ink)}
.blog .rule{left:100px;top:90px;width:265px;height:1px;background:var(--ink)}
.post{position:absolute;top:134px;width:487px;height:239px;background:var(--card);box-shadow:0 1px 3px rgba(0,0,0,.2)}
.post-photo{position:absolute;left:0;top:0;width:248px;height:239px}
.date{position:absolute;left:196px;top:16px;height:34px;display:flex}
.date .day{width:50px;background:var(--sky);font-size:22px;font-weight:700;text-align:center;line-height:34px}
.date .mon{width:52px;background:#6f6f6f;font-size:9px;font-weight:700;padding:5px 0 0 8px;line-height:11px}
.comments{position:absolute;left:398px;top:38px;display:flex;gap:6px;align-items:center;color:var(--ink);font-size:14px;font-weight:700}
.post h4{position:absolute;left:264px;top:90px;font-size:12px;font-weight:400;color:var(--ink);letter-spacing:.3px}
.post p{position:absolute;left:264px;top:114px;width:210px;font-size:11px;line-height:17px;color:#8a8a8a}
.post .btn{left:264px;top:167px;width:92px;height:28px;line-height:26px;border:none;font-size:12px}

/* footer */
.site-footer{top:2025px;height:264px;background:repeating-linear-gradient(90deg,var(--footer) 0 100px,#37312d 100px 200px)}
.f-col{position:absolute;top:38px}
.f-col h5{font-size:14px;font-weight:400;color:var(--white);padding-bottom:10px;border-bottom:1px solid #5a534e}
.f-divider{position:absolute;top:43px;width:1px;height:180px;background:#8a837d}
.contact-row{display:flex;align-items:center;gap:14px;margin-top:18px;font-size:11px;line-height:14px}
.ic{width:30px;height:30px;border-radius:50%;background:#6c6661;display:flex;align-items:center;justify-content:center;flex:none}
.phone{font-size:19px}
.news p{font-size:11px;line-height:17px;margin-top:8px}
.subscribe{position:absolute;left:0;top:118px;display:flex;height:31px}
.subscribe .field{width:155px;background:#5e5955;font-size:11px;line-height:31px;padding-left:28px;color:#d5d0cb}
.subscribe .go{width:95px;background:#1f1c1a;font-size:12px;font-weight:700;line-height:31px;text-align:center}
.links li{list-style:none;font-size:11px;margin-top:13px;display:flex;align-items:center;gap:8px}
.links li::before{content:"";border-left:5px solid var(--white);border-top:4px solid transparent;border-bottom:4px solid transparent}
.socials{display:flex;gap:8px;margin-top:18px}
.socials span{width:29px;height:29px}
.cards{display:flex;gap:10px;margin-top:18px;align-items:center}
.cards span{height:17px;border-radius:3px;background:#e9e9e9}
.legal{top:2289px;height:52px;background:var(--footer-bottom);font-size:11px;color:var(--muted)}
.legal .copy{left:100px;top:19px}
.legal .terms{left:886px;top:19px}
</style>
</head>
<body>

<header class="site-header">
  <div class="brand abs"><span class="brand-dot"></span><span class="brand-name">TrTr</span></div>
  <div class="brand-sub abs">lather company</div>
  <div class="util-box login abs">Log in | Sign Up</div>
  <div class="util-box currency abs">Pick a Currency<br><span class="select">USD ⇕</span></div>
  <div class="cart abs">
    <div class="cart-label">Your Cart</div>
    <div class="cart-count">0</div>
    <div class="cart-text">in your<br>cart</div>
  </div>
  <nav class="nav abs">
    <a style="left:266px">Home</a><span class="sep" style="left:315px"></span>
    <a style="left:375px">About Us</a><span class="sep" style="left:437px"></span>
    <a style="left:481px">Shop</a><span class="sep" style="left:528px"></span>
    <a style="left:614px">Who We Give ⌄</a><span class="sep" style="left:699px"></span>
    <a style="left:743px">Blog</a>
  </nav>
</header>

<section class="hero" role="img" aria-label="Photo of handmade natural soap bars tied with twine beside fresh green herbs">
  <div class="slide-arrow abs" style="left:3px;top:230px"><svg width="34" height="32"><path d="M20 9l-7 7 7 7" stroke="#fff" stroke-width="3" fill="none"/></svg></div>
  <div class="slide-arrow abs" style="left:1157px;top:230px"><svg width="34" height="32"><path d="M14 9l7 7-7 7" stroke="#fff" stroke-width="3" fill="none"/></svg></div>
  <div class="hero-caption abs">
    <h1>NATURAL SOAP</h1>
    <p>with out harmful chemicals</p>
  </div>
  <a class="btn">SHOP NOW</a>
</section>

<section class="about">
  <h2 class="title abs">ABOUT US</h2>
  <p class="about-text abs">Lorem ipsum dolor sit amet, consectetuer adipiscing elit, sed diam nonummy nibh euismod tincidunt ut laoreet dolore magna aliquam erat volutpat. Ut wisi enim ad minim veniam, quis nostrud exerci tation ullamcorper suscipit lobortis nisl ut aliquip ex ea commodo consequat. Duis autem vel eum iriure dolor in hendrerit in vulputate velit esse molestie consequat, vel illum dolore eu feugiat nulla facilisis at vero eros et accumsan et iusto odio dignissim qui blandit praesent luptatum zzril delenit augue duis dolore te feugait nulla facilisi.Lorem</p>
  <a class="btn">READ MORE</a>
</section>

<section class="products">
  <h2 class="title abs">LATEST PRODUCTS</h2>
  <div class="rule abs"></div>
  <svg class="abs" style="left:52px;top:252px" width="20" height="30"><path d="M14 4L5 15l9 11" stroke="#7fb2d6" stroke-width="3" fill="none"/></svg>
  <svg class="abs" style="left:1128px;top:252px" width="20" height="30"><path d="M6 4l9 11-9 11" stroke="#7fb2d6" stroke-width="3" fill="none"/></svg>

  <article class="product" style="left:120px">
    <div class="product-photo" role="img" aria-label="Photo of an olive oil soap bar with green olives on a wooden spoon" style="background:linear-gradient(135deg,#8a6a3e,#c9a46a 50%,#6e5a32)"></div>
    <h3>Lorem Ipsum Dolor</h3>
    <div class="product-meta"><span>🛒 ADD TO CART</span><b>$57.00</b></div>
    <div class="quick">+ QUICK VIEW</div>
  </article>
  <article class="product" style="left:451px">
    <div class="product-photo" role="img" aria-label="Photo of assorted handmade soap bars on a round metal tray" style="background:radial-gradient(circle,#b9a88c,#6d6a63 60%,#d8d6d2)"></div>
    <h3>Lorem Ipsum Dolor</h3>
    <div class="product-meta"><span>🛒 ADD TO CART</span><b>$57.00</b></div>
    <div class="quick">+ QUICK VIEW</div>
  </article>
  <article class="product" style="left:782px">
    <div class="product-photo" role="img" aria-label="Photo of lavender soap bars with dried lavender sprigs on white" style="background:linear-gradient(135deg,#ffffff,#eee6d2 55%,#d9c9a3)"></div>
    <h3>Lorem Ipsum Dolor</h3>
    <div class="product-meta"><span>🛒 ADD TO CART</span><b>$57.00</b></div>
    <div class="quick">+ QUICK VIEW</div>
  </article>
</section>

<section class="blog">
  <h2 class="title abs">LATEST BLOG</h2>
  <div class="rule abs"></div>

  <article class="post" style="left:100px">
    <div class="post-photo" role="img" aria-label="Photo of stacked herbal soap bars with roses and an oil bottle" style="background:linear-gradient(135deg,#a03a3a,#b8875a 45%,#4f6a3a)"></div>
    <div class="date"><span class="day">05</span><span class="mon">JULY<br>2016</span></div>
    <div class="comments"><svg width="30" height="22"><ellipse cx="12" cy="9" rx="10" ry="7" fill="none" stroke="#7fb2d6" stroke-width="2.5"/><path d="M6 15l-3 5 7-3" fill="#7fb2d6"/><path d="M22 6a8 6 0 0 1 4 12l2 4-6-2" fill="none" stroke="#7fb2d6" stroke-width="2"/></svg>1,256</div>
    <h4>LOREM : IPSUM IS SIMPLY DUMMY</h4>
    <p>Contrary to popular belief, Lorem Ipsum is not simply random text.</p>
    <a class="btn">MORE</a>
  </article>
  <article class="post" style="left:615px">
    <div class="post-photo" role="img" aria-label="Photo of purple and cream lavender soap bars with lavender flowers" style="background:linear-gradient(160deg,#5d5a8e,#e8dcc0 45%,#8a6a9a)"></div>
    <div class="date"><span class="day">05</span><span class="mon">April<br>2016</span></div>
    <div class="comments"><svg width="30" height="22"><ellipse cx="12" cy="9" rx="10" ry="7" fill="none" stroke="#7fb2d6" stroke-width="2.5"/><path d="M6 15l-3 5 7-3" fill="#7fb2d6"/><path d="M22 6a8 6 0 0 1 4 12l2 4-6-2" fill="none" stroke="#7fb2d6" stroke-width="2"/></svg>1,256</div>
    <h4>LOREM : IPSUM IS SIMPLY DUMMY</h4>
    <p>Contrary to popular belief, Lorem Ipsum is not simply random text.</p>
    <a class="btn">MORE</a>
  </article>
</section>

<footer class="site-footer">
  <div class="f-col" style="left:98px;width:210px">
    <h5 style="border:none">CONTACT US</h5>
    <div class="contact-row" style="margin-top:14px"><span class="ic"><svg width="14" height="18"><path d="M7 1a6 6 0 0 1 6 6c0 4-6 10-6 10S1 11 1 7a6 6 0 0 1 6-6z" fill="#fff"/><circle cx="7" cy="7" r="2.2" fill="#6c6661"/></svg></span><span>Lorem ipsum dolor sit amet,<br>consectetuer adipiscing elit</span></div>
    <div class="contact-row"><span class="ic"><svg width="16" height="16"><path d="M3 1l3 0 1 4-2 1a9 9 0 0 0 5 5l1-2 4 1v3c0 1-1 2-2 2C7 15 1 9 1 3c0-1 1-2 2-2z" fill="#fff"/></svg></span><span class="phone">123-456-7890</span></div>
    <div class="contact-row"><span class="ic"><svg width="16" height="12"><rect x="0" y="0" width="16" height="12" rx="1" fill="#fff"/><path d="M1 1l7 6 7-6" stroke="#6c6661" stroke-width="1.5" fill="none"/></svg></span><span>support@trtrlathercompany.com</span></div>
  </div>
  <div class="f-divider" style="left:340px"></div>

  <div class="f-col news" style="left:387px;width:250px">
    <h5>NEWSLETTER SIGNUP</h5>
    <p>Get the latest updates<br>by entering your<br>email address</p>
    <svg class="abs" style="left:145px;top:42px" width="70" height="64"><path d="M2 28L66 6 36 60 28 38z" fill="#d9d4cf"/><path d="M28 38L66 6" stroke="#7e7872" stroke-width="1.5"/><path d="M28 38l-2 18 10-14" fill="#a9a39d"/></svg>
    <div class="subscribe"><span class="field">Enter your email here</span><span class="go">SUBSCRIBE</span></div>
    <svg class="abs" style="left:8px;top:129px" width="14" height="10"><rect width="14" height="10" rx="1" fill="#d5d0cb"/><path d="M1 1l6 5 6-5" stroke="#5e5955" fill="none"/></svg>
  </div>
  <div class="f-divider" style="left:677px"></div>

  <div class="f-col" style="left:722px;width:115px">
    <h5>ABOUT US</h5>
    <ul class="links"><li>Home</li><li>About Us</li><li>Shop</li><li>Who We Give</li><li>Blog</li></ul>
  </div>
  <div class="f-divider" style="left:882px"></div>

  <div class="f-col" style="left:927px;width:175px">
    <h5>FOLLOW US</h5>
    <div class="socials"><span style="background:#3b5b9a"></span><span style="background:#2a9ee0"></span><span style="background:#d34836"></span><span style="background:#d9332a"></span></div>
    <h5 style="border:none;margin-top:22px;padding:0">WE ACCEPT</h5>
    <div class="cards"><span style="width:36px"></span><span style="width:22px;border-radius:50%"></span><span style="width:20px;background:#8bb6da"></span><span style="width:52px"></span></div>
  </div>
</footer>

<section class="legal">
  <span class="copy abs">Copyright 2016 Trtrlathercompany. All Rights Reserved.</span>
  <span class="terms abs">Terms &amp; Conditions &nbsp;&nbsp; | &nbsp;&nbsp; Privacy Policy</span>
</section>

</body>
</html>
```